Tidewell Hypnotherapy 2017 DL Card Flyer

We would like a double sided DL Card Flyer design.

We are a professional Hypnotherapy Clinic looking for a fresh clean design.

Front of card is summary info and back of flyer is detailed text.

I have attached documents with text for the front (dl size hypno 1) and back (dl size hypno 2) of the card and an indicative style of layout.

There are logo files uploaded as well as one image file.

The colors we like are blue, white and yellow/gold.
Updates

please note: when using the 'bright steps bold change' image, please only use the top half of the image. The girl is not to be in the image, just the words and light bulb with the chalk underline. thanks.. Added Sunday, March 19, 2017

Industry/Entity Type

Health And Wellness

Requirements
Must have
• Note. I have misspelled the www.TidewellHypnotherapy.com.au (missing an 'o' in the attachments to the brief). My error. Please amend in your design submissions.

```html
<!DOCTYPE html>
<html lang="en">
<head>
<meta charset="utf-8">
<title>Tidewell Hypnotherapy DL Flyer</title>
<link href="https://fonts.googleapis.com/css2?family=Montserrat:wght@400;500;600;700&family=Courgette&display=swap" rel="stylesheet">
<style>
  :root{
    --navy:#27306b;
    --navy-deep:#1e2558;
    --grey:#8c8c8c;
    --grey-light:#d9d9d9;
    --bg:#e6e6e6;
    --white:#ffffff;
    --red:#e0201f;
    --ink:#2b2b2b;
    --chalk-dark:#2e2f31;
    --chalk-mid:#4a4c4f;
    --bulb:#f3d35a;
  }
  *{box-sizing:border-box;margin:0;padding:0}
  html,body{width:1200px;height:1200px;overflow:hidden}
  body{background:var(--bg);font-family:"Montserrat",Arial,sans-serif;color:var(--ink);position:relative}
  .card{position:absolute;top:180px;width:400px;height:840px;background:var(--white);overflow:hidden;box-shadow:0 4px 14px rgba(0,0,0,.18)}
  .card--front{left:170px}
  .card--back{left:630px;padding:18px 22px 0}

  /* front */
  .brand{position:absolute;left:26px;top:30px;display:flex;align-items:center;gap:14px}
  .brand__dot{width:54px;height:54px;border-radius:50%;background:var(--navy)}
  .brand__name{font-weight:700;color:var(--navy);font-size:20px;line-height:1.05;letter-spacing:.5px;border-left:1px solid var(--grey);padding-left:12px}
  .quote{position:absolute;left:0;right:20px;top:100px;text-align:right;font-family:"Courgette",cursive;font-size:17px;color:var(--navy);line-height:1.25}
  .quote em{font-style:normal;color:var(--red)}
  .hero{position:absolute;left:0;top:165px;width:400px;height:215px;background:radial-gradient(circle at 50% 35%,#6b6a5a 0,var(--chalk-mid) 28%,var(--chalk-dark) 80%)}
  .wave{position:absolute;left:0;width:400px}
  .wave--top{top:140px;height:60px}
  .wave--bottom{top:340px;height:60px}
  .programs{position:absolute;left:0;top:390px;width:400px;height:330px;background:var(--navy);padding:12px 28px 0 32px;color:var(--white)}
  .programs__title{font-size:19px;font-weight:700;line-height:1.3;letter-spacing:.6px;margin-bottom:22px}
  .programs__list{list-style:none}
  .programs__list li{display:flex;align-items:center;gap:12px;font-size:15px;font-weight:600;margin-bottom:13px}
  .programs__list li span{font-weight:400}
  .programs__list svg{flex:none}
  .contact{position:absolute;left:0;top:720px;width:400px;height:120px;display:flex;align-items:center;gap:16px;padding-left:24px}
  .contact__dot{width:66px;height:66px;border-radius:50%;background:var(--navy)}
  .contact__phone{font-size:34px;font-weight:700;color:var(--navy);letter-spacing:1px;line-height:1}
  .contact__web{font-size:12px;font-weight:600;color:var(--navy);margin-top:8px}

  /* back */
  .program{margin-bottom:10px}
  .program__head{background:var(--navy);color:var(--white);font-size:11px;font-weight:700;text-align:center;padding:7px 6px;letter-spacing:.4px;line-height:1.3}
  .program__head span{font-weight:400}
  .program__body{font-size:10px;line-height:1.4;padding:7px 8px 0;text-align:justify}
  .program__sessions{font-size:10px;font-weight:700;padding:4px 8px 0}
  .note{background:var(--grey);color:var(--white);border-radius:12px;font-size:10.5px;font-weight:600;padding:10px 14px;margin-top:12px;line-height:1.4}
  .back-web{text-align:center;font-size:11px;margin-top:12px;color:var(--ink)}
</style>
</head>
<body>

<section class="card card--front">
  <div class="brand">
    <div class="brand__dot"></div>
    <div class="brand__name">TIDEWELL<br>HYPNOTHERAPY</div>
  </div>
  <p class="quote">“There is nothing more<br>important than <em>good health</em>”</p>

  <div class="hero" role="img" aria-label="Chalkboard with a glowing light bulb and the chalk words bright steps bold change"></div>
  <svg class="wave wave--top" viewBox="0 0 400 60" preserveAspectRatio="none">
    <path d="M0 60 L0 20 C120 -5 260 -5 400 28 L400 60 Z" fill="var(--grey)"/>
    <path d="M0 60 L0 30 C120 10 260 12 400 40 L400 60 Z" fill="var(--navy)"/>
    <path d="M0 0 L400 0 L400 28 C260 -5 120 -5 0 20 Z" fill="var(--white)"/>
    <path d="M0 60 L0 42 C130 26 270 30 400 56 L400 60 Z" fill="var(--chalk-dark)"/>
  </svg>
  <svg class="wave wave--bottom" viewBox="0 0 400 60" preserveAspectRatio="none">
    <path d="M0 60 L0 40 C120 10 260 30 400 0 L400 60 Z" fill="var(--navy)"/>
  </svg>

  <div class="programs">
    <h2 class="programs__title">PROFESSIONAL HYPNOSIS<br>THERAPY PROGRAMS:</h2>
    <ul class="programs__list">
      <li><svg width="16" height="16" viewBox="0 0 16 16"><rect x="1" y="3" width="12" height="12" fill="none" stroke="#fff" stroke-width="1.4"/><path d="M4 9 L7 12 L15 1" fill="none" stroke="#fff" stroke-width="1.6"/></svg>Weight Loss <span>(Virtual Gastric Band)</span></li>
      <li><svg width="16" height="16" viewBox="0 0 16 16"><rect x="1" y="3" width="12" height="12" fill="none" stroke="#fff" stroke-width="1.4"/><path d="M4 9 L7 12 L15 1" fill="none" stroke="#fff" stroke-width="1.6"/></svg>Sugar Addiction</li>
      <li><svg width="16" height="16" viewBox="0 0 16 16"><rect x="1" y="3" width="12" height="12" fill="none" stroke="#fff" stroke-width="1.4"/><path d="M4 9 L7 12 L15 1" fill="none" stroke="#fff" stroke-width="1.6"/></svg>Quit Smoking</li>
      <li><svg width="16" height="16" viewBox="0 0 16 16"><rect x="1" y="3" width="12" height="12" fill="none" stroke="#fff" stroke-width="1.4"/><path d="M4 9 L7 12 L15 1" fill="none" stroke="#fff" stroke-width="1.6"/></svg>Chronic Fatigue &amp; Chronic Pain Relief</li>
      <li><svg width="16" height="16" viewBox="0 0 16 16"><rect x="1" y="3" width="12" height="12" fill="none" stroke="#fff" stroke-width="1.4"/><path d="M4 9 L7 12 L15 1" fill="none" stroke="#fff" stroke-width="1.6"/></svg>Stress Relief &amp; Deep Relaxation</li>
    </ul>
  </div>

  <div class="contact">
    <div class="contact__dot"></div>
    <div>
      <div class="contact__phone">1300 555 014</div>
      <div class="contact__web">www.TidewellHypnotherapy.com.au</div>
    </div>
  </div>
</section>

<section class="card card--back">
  <article class="program">
    <h3 class="program__head">WEIGHT LOSS PROGRAM <span>(Virtual Gastric Band)</span></h3>
    <p class="program__body">Achieve long term weight loss without dieting. Whether it's losing 3kg or 30kg, we'll help you become the shape and size you want to be. Our Internationally Accredited Program is proven to be 95% effective in clinical trials.</p>
    <p class="program__sessions">Number of Sessions: 6+</p>
  </article>
  <article class="program">
    <h3 class="program__head">SUGAR ADDICTION PROGRAM</h3>
    <p class="program__body">Excess sugar intake can lead to obesity, Type 2 Diabetes and tooth decay. The habit of reaching for soft drinks, chocolate, sweets, cakes and biscuits can be hard to break. By rewiring your subconscious habits, our Program puts you back in control.</p>
    <p class="program__sessions">Number of Sessions: 3+</p>
  </article>
  <article class="program">
    <h3 class="program__head">QUIT SMOKING PROGRAM</h3>
    <p class="program__body">The facts speak for themselves. You are 10 times more likely to quit smoking for good using hypnotherapy. Expect to be a non smoker after completing the first session of our Program. (12 Month Guarantee)</p>
    <p class="program__sessions">Number of Sessions: 2</p>
  </article>
  <article class="program">
    <h3 class="program__head">CHRONIC FATIGUE &amp;<br>CHRONIC PAIN RELIEF PROGRAM</h3>
    <p class="program__body">Chronic Fatigue, Fibromyalgia and Chronic Musculoskeletal Pain are diseases of modern living. The symptoms of fatigue and pain are very real, however the cause is usually emotional, and is generally hidden beyond our conscious awareness.<br>Our Program comprises Education and Hypnosis to help you regain your health, your self esteem, your friends and your life, all in a manageable timeframe.</p>
    <p class="program__sessions">Number of Sessions: 6+</p>
  </article>
  <article class="program">
    <h3 class="program__head">STRESS RELIEF &amp; DEEP RELAXATION PROGRAM</h3>
    <p class="program__body">Our Program gently uncovers the true source of your stress, and helps you reconnect to a natural inner calm. We teach you self hypnosis so that you have the tools to continue your experience.</p>
    <p class="program__sessions">Number of Sessions: 3+</p>
  </article>
  <p class="note">All Programs include take home CD's personally recorded by our therapists, using advanced hypnotic techniques.</p>
  <p class="back-web">www.TidewellHypnotherapy.com.au</p>
</section>

</body>
</html>
```